Rw building ventures pty ltd

This is a development and construction company. Website can be set up on our domain rwbuildworks.net if we could change the domain to rwbuildworks.com.au would be great

Want the page to have eye catching designs, red, black and white are the preffered colours.

Check out www.toluqin.com.au it is my former company with my partner which i am now venturing out on my own, that is the perfect example of the website i want even allot of the information would be the same

Industry/Entity Type

Construction

Coding

Coded - Design and coding required

Number of Pages Required

5+ page

Requirements
Must have
• Company logo eye catching designs

```html
<!DOCTYPE html>
<html lang="en">
<head>
<meta charset="utf-8">
<title>RW Buildworks – Development &amp; Construction</title>
<link href="https://fonts.googleapis.com/css2?family=Quicksand:wght@500;600;700&family=Lato:wght@400;700&display=swap" rel="stylesheet">
<style>
:root{
  --red:#e8401c;
  --black:#141414;
  --dark:#1b1b1d;
  --white:#ffffff;
  --ink:#2a2a2a;
  --muted:#555;
  --line:#d9d9d9;
  --card:#f3f3f3;
}
*{margin:0;padding:0;box-sizing:border-box}
html,body{width:1200px;height:4902px;overflow:hidden}
body{position:relative;background:var(--white);font-family:'Lato',sans-serif;color:var(--ink);font-size:12.5px;line-height:22px}
.abs{position:absolute}
.heading{font-family:'Quicksand',sans-serif;font-weight:600;color:var(--black)}
.pill{position:absolute;display:flex;align-items:center;justify-content:center;gap:10px;border-radius:20px;font-size:12.5px;color:var(--white);background:var(--red)}
.photo{position:absolute}
p{margin:0}

/* header */
.site-header{position:absolute;left:0;top:0;width:1200px;height:146px;background:var(--white)}
.brand{position:absolute;display:flex;align-items:center;gap:10px;font-family:'Quicksand',sans-serif;font-weight:700;letter-spacing:1px}
.brand-mark{width:14px;height:14px;background:var(--red)}
.nav a{position:absolute;top:70px;font-size:13px;color:var(--ink);text-decoration:none}
.nav a.active{color:var(--red)}
.nav a.active::after{content:"";position:absolute;left:0;right:0;bottom:-6px;height:2px;background:var(--red)}
.quote-btn{left:970px;top:59px;width:156px;height:34px;background:linear-gradient(90deg,var(--red) 55%,var(--black) 55%)}

/* hero */
.hero{position:absolute;left:0;top:146px;width:1200px;height:611px;background:linear-gradient(180deg,#4d6478 0%,#a6b1ba 35%,#d8d6d0 55%,#3a3a3a 80%,#262626 100%)}
.hero-title{position:absolute;left:97px;top:222px;font-family:'Quicksand',sans-serif;font-weight:500;font-size:35px;line-height:40px;color:var(--white)}
.hero-sub{position:absolute;left:97px;top:308px;font-size:14px;letter-spacing:1px;color:var(--white)}
.btn-outline{position:absolute;left:99px;top:339px;width:152px;height:38px;border:2px solid var(--white);border-radius:20px;color:var(--white);font-size:13px;display:flex;align-items:center;justify-content:center}
.play{position:absolute;left:268px;top:339px;width:38px;height:38px;border-radius:50%;background:var(--red)}
.watch{position:absolute;left:325px;top:347px;color:var(--white);font-size:13px}
.dots span{position:absolute;left:1143px;width:24px;height:24px;border-radius:50%;background:rgba(255,255,255,.7);font-size:10px;line-height:24px;text-align:center;color:var(--ink)}
.dots span.on{background:var(--white);color:var(--red);border:1px solid var(--red)}
.scroll-notch{position:absolute;left:568px;top:586px;width:64px;height:34px;border-radius:32px 32px 0 0;background:var(--white)}

/* about */
.section-title{position:absolute;left:0;width:1200px;text-align:center;font-size:30px}
.rule{position:absolute;height:3px;background:var(--red)}
.about-text{position:absolute;left:631px;width:462px}

/* services */
.services{position:absolute;left:0;top:1417px;width:1200px;height:609px;background:linear-gradient(160deg,#2a2a2c,#0f0f10 60%,#222)}
.service-card{position:absolute;top:1550px;width:304px;height:320px;background:var(--white);border-radius:4px;text-align:center}
.service-card.featured{background:var(--red);color:var(--white)}
.service-card h3{position:absolute;top:152px;width:100%;font-family:'Quicksand',sans-serif;font-weight:600;font-size:19px}
.service-card p{position:absolute;top:187px;left:36px;right:36px;font-size:12px;line-height:22px}
.service-card svg.arrow{position:absolute;left:140px;top:278px}
.service-card svg.icon{position:absolute;left:112px;top:44px}

/* projects */
.tile{position:absolute}
.tile-caption{position:absolute;left:24px;bottom:26px;color:var(--white);font-size:13px;line-height:17px;text-transform:uppercase}

/* quality */
.quality{position:absolute;left:0;top:2811px;width:1200px;height:609px;background:linear-gradient(160deg,#232325,#111 55%,#2a2a2a)}

/* partners */
.partner-card{position:absolute;top:3625px;width:312px;height:255px;background:var(--card);border-radius:4px;text-align:center}
.partner-card .name{position:absolute;top:91px;width:100%;font-size:13px;color:var(--ink)}
.partner-card .place{position:absolute;top:106px;width:100%;font-size:13px;color:var(--red)}
.partner-card p{position:absolute;top:138px;left:30px;right:30px;font-size:12.5px;line-height:19px;color:var(--muted)}
.avatar{position:absolute;top:3563px;width:114px;height:114px;border-radius:50%;background:radial-gradient(circle at 50% 40%,#cfd3d6,#8a9096);border:4px solid var(--white)}

/* contact form */
.field{position:absolute;border:1px solid #c9c9c9;background:var(--white);font-size:12.5px;color:#666;padding:10px 14px;line-height:20px}

/* footer */
.site-footer{position:absolute;left:0;top:4470px;width:1200px;height:365px;background:linear-gradient(180deg,#1a1a1a,#0c0c0c)}
.footer-col{position:absolute;color:var(--white);font-size:12.5px}
.footer-col h4{font-family:'Quicksand',sans-serif;font-weight:600;font-size:14px;margin-bottom:10px}
.footer-col .bar{width:36px;height:2px;background:var(--red);margin-bottom:16px}
.links li{list-style:none;height:25.5px;position:relative;padding-left:18px;font-size:12px}
.links li::before{content:"";position:absolute;left:2px;top:10px;width:4px;height:4px;border-radius:50%;background:var(--white)}
.bottom-bar{position:absolute;left:0;top:4835px;width:1200px;height:67px;background:var(--white)}
.social span{position:absolute;top:4856px;width:30px;height:30px;border-radius:50%;background:var(--black)}
</style>
</head>
<body>

<!-- header -->
<header class="site-header">
  <div class="brand" style="left:72px;top:52px;font-size:26px;color:var(--black)"><span class="brand-mark"></span>RW BUILDWORKS</div>
  <nav class="nav">
    <a class="active" style="left:478px">Home</a>
    <a style="left:549px">About</a>
    <a style="left:620px">Our Services</a>
    <a style="left:730px">Projects</a>
    <a style="left:810px">Partner</a>
    <a style="left:886px">Contact</a>
  </nav>
  <div class="pill quote-btn">Get A Quote
    <svg width="44" height="10" viewBox="0 0 44 10"><path d="M0 5H42M36 1L42 5L36 9" stroke="#fff" stroke-width="1.6" fill="none"/></svg>
  </div>
</header>

<!-- hero -->
<section class="hero" role="img" aria-label="Photograph of a modern two-storey white house with large glass windows under a cloudy sky"></section>
<h1 class="hero-title" style="top:368px">Development &amp;<br>Construction Company</h1>
<div class="hero-sub" style="top:454px">CONSTRUCTION – HOUSE BUILDS – RENOVATION</div>
<div class="btn-outline" style="top:485px">View Project</div>
<div class="play" style="top:485px"><svg width="38" height="38" viewBox="0 0 38 38"><path d="M16 13L25 19L16 25Z" fill="#fff"/></svg></div>
<div class="watch" style="top:493px">Watch Video</div>
<div class="dots">
  <span style="top:405px">01</span>
  <span class="on" style="top:439px">02</span>
  <span style="top:471px">03</span>
  <span style="top:503px">04</span>
</div>
<div class="scroll-notch"><svg width="64" height="34" viewBox="0 0 64 34"><path d="M26 15L32 21L38 15" stroke="#222" stroke-width="2" fill="none"/></svg></div>

<!-- about -->
<h2 class="heading section-title" style="top:866px">About us</h2>
<div class="rule" style="left:566px;top:922px;width:68px"></div>
<div class="photo" style="left:114px;top:960px;width:462px;height:337px;border-radius:6px;background:linear-gradient(160deg,#c9d4dd,#9ba6ad 45%,#5b4a3c 75%,#3b3b3b)" role="img" aria-label="Photograph of modern terrace townhouses with curved white balconies and timber cladding"></div>
<div class="about-text" style="top:958px;font-size:13px;line-height:22px;color:var(--black)">Welcome to<br><strong>Development &amp; Construction Company</strong></div>
<div class="about-text" style="top:1014px">Lorem Ipsum is simply dummy text of the printing and typesetting industry has been the industry's standard dummy text ever since the 1500s, when an unknown printer took a galley of type and scrambled it to make a type specimen book. It has survived not only five centuries, but also the leap into electronic typesetting, remaining essentially unchanged. It was popularised in the 1960s</div>
<div class="about-text" style="top:1168px">with the release of Letraset sheets containing Lorem Ipsum passages, and more recently with desktop publishing software like Aldus PageMaker including into electronic typesetting, remaining essentially unchanged.</div>
<div class="pill" style="left:633px;top:1257px;width:154px;height:40px">Read More</div>

<!-- services -->
<section class="services"></section>
<h2 class="heading section-title" style="top:1480px;color:var(--white)">Our Services</h2>

<div class="service-card" style="left:116px">
  <svg class="icon" width="80" height="90" viewBox="0 0 80 90" fill="none" stroke="#e8401c" stroke-width="2.5"><rect x="6" y="10" width="68" height="74"/><path d="M22 50L40 34L58 50V72H22Z"/><rect x="34" y="56" width="12" height="16"/></svg>
  <h3>Construction</h3>
  <p>Lorem Ipsum is simply dummy text of the printing and typesetting industry has been the industry's.</p>
  <svg class="arrow" width="26" height="16" viewBox="0 0 26 16"><path d="M0 8H24M17 1L24 8L17 15" stroke="#e8401c" stroke-width="2" fill="none"/></svg>
</div>
<div class="service-card featured" style="left:451px">
  <svg class="icon" width="80" height="90" viewBox="0 0 80 90" fill="none" stroke="#fff" stroke-width="2.5"><path d="M10 20H74M20 20V84M10 84H74"/><path d="M30 56L48 42L66 56V84H30Z"/><rect x="42" y="66" width="12" height="18"/></svg>
  <h3>House Builds</h3>
  <p>Lorem Ipsum is simply dummy text of the printing and typesetting industry has been the industry's.</p>
  <svg class="arrow" width="26" height="16" viewBox="0 0 26 16"><path d="M0 8H24M17 1L24 8L17 15" stroke="#fff" stroke-width="2" fill="none"/></svg>
</div>
<div class="service-card" style="left:784px">
  <svg class="icon" width="80" height="90" viewBox="0 0 80 90" fill="none" stroke="#e8401c" stroke-width="2.5"><path d="M4 44L40 10L76 44"/><path d="M14 36V84H66V36"/><path d="M28 72L52 48M28 48L52 72"/></svg>
  <h3>Renovation</h3>
  <p>Lorem Ipsum is simply dummy text of the printing and typesetting industry has been the industry's.</p>
  <svg class="arrow" width="26" height="16" viewBox="0 0 26 16"><path d="M0 8H24M17 1L24 8L17 15" stroke="#e8401c" stroke-width="2" fill="none"/></svg>
</div>
<div class="pill" style="left:529px;top:1910px;width:154px;height:38px">View More
  <svg width="40" height="10" viewBox="0 0 40 10"><path d="M0 5H38M32 1L38 5L32 9" stroke="#fff" stroke-width="1.6" fill="none"/></svg>
</div>

<!-- projects -->
<div class="abs" style="left:0;top:2100px;width:1200px;text-align:center;font-size:12.5px;color:var(--ink)">Our Latest</div>
<h2 class="heading section-title" style="top:2120px">Projects</h2>
<div class="tile" style="left:116px;top:2201px;width:262px;height:215px;background:linear-gradient(180deg,#e9eef2,#cfc6bc 60%,#a8917c)" role="img" aria-label="Photograph of a bright bedroom with a patterned rug"></div>
<div class="tile" style="left:397px;top:2201px;width:263px;height:215px;background:linear-gradient(180deg,#e8e8e8,#6d6562 45%,#f1f1f1)" role="img" aria-label="Photograph of a kitchen with dark cabinetry and white benchtop"></div>
<div class="tile" style="left:116px;top:2440px;width:262px;height:213px;background:linear-gradient(180deg,#e2e2e0,#bcae9a 45%,#e7e7e7)" role="img" aria-label="Photograph of a kitchen island with bar stools"></div>
<div class="tile" style="left:397px;top:2440px;width:263px;height:213px;background:linear-gradient(180deg,#bfbfbf,#4a3d37 50%,#d8d8d8)" role="img" aria-label="Photograph of an entry hallway with dark timber slats"></div>
<div class="tile" style="left:679px;top:2201px;width:407px;height:452px;border:2px solid var(--red);background:linear-gradient(180deg,#5a7fa8,#9aa6b0 30%,#8b8b87 65%,#4e4e4d)" role="img" aria-label="Photograph of a grey two-storey duplex home with garage">
  <div class="tile-caption">Harbourline Road,<br>Greystead</div>
  <svg class="abs" style="right:20px;bottom:22px" width="40" height="40" viewBox="0 0 40 40" fill="none" stroke="#fff" stroke-width="1.6"><path d="M2 12V2H12M28 2H38V12M38 28V38H28M12 38H2V28M2 2L14 14M38 2L26 14M38 38L26 26M2 38L14 26"/></svg>
</div>
<div class="pill" style="left:529px;top:2684px;width:152px;height:38px">View More</div>

<!-- quality -->
<section class="quality"></section>
<h2 class="heading abs" style="left:112px;top:2922px;font-size:32px;line-height:34px;color:var(--white)">Qualtiy,<br>Innovation &amp; Excellence</h2>
<div class="abs" style="left:112px;top:2995px;width:470px;height:2px;background:rgba(255,255,255,.15)"></div>
<p class="abs" style="left:112px;top:3028px;width:470px;color:var(--white)">Lorem Ipsum is simply dummy text of the printing and typesetting industry has been the industry's standard dummy text ever since the 1500s, when an unknown printer took a galley of type and scrambled it to make a type specimen book. It has survived not only five centuries, but also the leap into electronic typesetting, remaining essentially unchanged. It was popularised in the 1960s</p>
<p class="abs" style="left:112px;top:3182px;width:470px;color:var(--white)">with the release of Letraset sheets containing Lorem Ipsum passages, and more recently with desktop publishing software like Aldus PageMaker including into electronic typesetting, remaining essentially unchanged.</p>
<div class="pill" style="left:116px;top:3281px;width:152px;height:36px">Read More</div>
<div class="abs" style="left:685px;top:2938px;width:418px;height:390px;border:2px solid var(--red);border-radius:4px"></div>
<div class="photo" style="left:647px;top:2910px;width:439px;height:409px;border-radius:4px;background:linear-gradient(180deg,#4f86c6,#b9cde0 30%,#e6e6e4 55%,#a07d62 85%,#7a6e66)" role="img" aria-label="Photograph of a modern white home with timber battens and glass balcony"></div>

<!-- partners -->
<div class="abs" style="left:0;top:3485px;width:1200px;text-align:center;font-size:12.5px">From Our</div>
<h2 class="heading section-title" style="top:3506px">Our Partner</h2>
<div class="partner-card" style="left:116px">
  <div class="name">Marco Delvane</div><div class="place">Ashgrove</div>
  <p>Lorem Ipsum is simply dummy text of the printing and typesetting industry has been the industry's standard dummy text ever since the 1500s/</p>
</div>
<div class="partner-card" style="left:447px;box-shadow:0 4px 14px rgba(0,0,0,.12)">
  <div class="name">Peter Lanford</div><div class="place">Fairhill East</div>
  <p>Lorem Ipsum is simply dummy text of the printing and typesetting industry has been the industry's standard dummy text ever since the 1500s/</p>
</div>
<div class="partner-card" style="left:778px">
  <div class="name">Daniel Orrin</div><div class="place">Kellbrook</div>
  <p>Lorem Ipsum is simply dummy text of the printing and typesetting industry has been the industry's standard dummy text ever since the 1500s/</p>
</div>
<div class="avatar" style="left:211px" role="img" aria-label="Portrait photo of partner"></div>
<div class="avatar" style="left:542px" role="img" aria-label="Portrait photo of partner"></div>
<div class="avatar" style="left:875px" role="img" aria-label="Portrait photo of partner"></div>
<div class="abs" style="left:540px;top:3919px;width:20px;height:2px;background:#333"></div>
<div class="abs" style="left:566px;top:3918px;width:34px;height:4px;background:var(--red)"></div>
<div class="abs" style="left:606px;top:3919px;width:20px;height:2px;background:#333"></div>
<div class="abs" style="left:632px;top:3919px;width:20px;height:2px;background:#333"></div>

<!-- quick contact -->
<h2 class="heading abs" style="left:116px;top:4024px;font-size:32px">Quick Contact</h2>
<div class="rule" style="left:116px;top:4080px;width:34px"></div>
<div class="field" style="left:116px;top:4103px;width:219px;height:45px">Name*</div>
<div class="field" style="left:116px;top:4166px;width:219px;height:45px">Phone*</div>
<div class="field" style="left:116px;top:4232px;width:219px;height:45px">Email*</div>
<div class="field" style="left:348px;top:4101px;width:217px;height:177px">Message</div>
<div class="pill" style="left:116px;top:4310px;width:152px;height:38px">Send</div>
<div class="photo" style="left:622px;top:4004px;width:474px;height:352px;background:linear-gradient(180deg,#f0f0f0,#b58a62 30%,#ece9e4 55%,#b07f55 75%,#e6e6e6)" role="img" aria-label="Rendered 3D floor plan of a two-level home"></div>

<!-- footer -->
<footer class="site-footer"></footer>
<div class="brand" style="left:72px;top:4644px;font-size:26px;color:var(--white)"><span class="brand-mark"></span>RW BUILDWORKS</div>
<div class="footer-col" style="left:417px;top:4564px">
  <h4>Quick Links</h4><div class="bar"></div>
  <ul class="links">
    <li><strong>Home</strong></li><li>About</li><li>Service</li><li>Projects</li><li>Partner</li><li>Contact</li>
  </ul>
</div>
<div class="footer-col" style="left:609px;top:4564px;font-size:12px">
  <h4>Quick Contact</h4><div class="bar" style="margin-bottom:10px"></div>
  <div style="position:relative;padding-left:26px;line-height:25px">
    <svg class="abs" style="left:2px;top:4px" width="12" height="16" viewBox="0 0 12 16" fill="none" stroke="#fff" stroke-width="1.3"><path d="M6 15C6 15 1 9 1 6A5 5 0 0 1 11 6C11 9 6 15 6 15Z"/><circle cx="6" cy="6" r="2"/></svg>
    48 Harlow Street, Brookvale,<br>NSW 2100,<br>Australia
  </div>
  <div style="position:relative;padding-left:26px;margin-top:14px;line-height:25px">
    <svg class="abs" style="left:0;top:6px" width="16" height="12" viewBox="0 0 16 12" fill="none" stroke="#fff" stroke-width="1.3"><rect x="1" y="1" width="14" height="10" rx="2"/><path d="M4 4H12M4 7H12"/></svg>
    00 987 654 3210
  </div>
  <div style="position:relative;padding-left:26px;line-height:25px">
    <svg class="abs" style="left:0;top:7px" width="16" height="12" viewBox="0 0 16 12" fill="none" stroke="#fff" stroke-width="1.3"><rect x="1" y="1" width="14" height="10"/><path d="M1 1L8 7L15 1"/></svg>
    info@rwbuildworks.com.au
  </div>
</div>
<div class="footer-col" style="left:898px;top:4564px;width:226px">
  <h4>Newsletter</h4><div class="bar" style="margin-bottom:8px"></div>
  <p style="font-size:12.5px;line-height:17px">Lorem Ipsum is simply dummy text and typesetting industry.</p>
</div>
<div class="abs" style="left:898px;top:4679px;width:226px;height:34px;border-radius:17px;background:var(--white);font-size:12px;color:#777;font-style:italic;padding:7px 18px">Your Email Address</div>
<div class="pill" style="left:898px;top:4723px;width:226px;height:32px;font-size:12px">SUBSCRIBE</div>

<div class="bottom-bar"></div>
<div class="abs" style="left:72px;top:4860px;font-size:12px;color:var(--ink)">Copyright © 2021 <span style="color:var(--red)">RW BUILDWORKS</span>. All Rights Reserved</div>
<div class="social">
  <span style="left:982px;background:var(--red)"></span>
  <span style="left:1020px"></span>
  <span style="left:1058px"></span>
  <span style="left:1096px"></span>
</div>

</body>
</html>
```